I want a flyer for a company that changes Incandescent bulbs and halogen bulbs in LED. The flyer can content this information and benefits that the LED can “give” you : With the help of LED's you will save up to 90% of the electricity bill, it helps the planet! They don't contain mercury, release carbon dioxide, they resist at lower temperatures, aren't sensitive to humidity, there haven't been any registered case of catching fire, release a bad odor or smoke from them, unlike incandescent and halogen bulbs. Their life spend is higher than 25000 hours! 5 years warranty

Do you want a better life? Do you want to help the planet? Do you want to save money? The LED light bulbs are the solution!
Discover the new and revolutionary way of illuminating your house with the help of LED light bulbs.

These are suggestions, you can do anything you can believe is better, I have no experience in advertising. My supplier is www.glowvane.co.uk , you can have a look there.

This leaflets will be distributed to the potential customers thru their post boxes.

I want to start the campaign ASAP, so waiting your ideas!!!

Industry/Entity Type

It Company

```html
<!DOCTYPE html>
<html lang="en">
<head>
<meta charset="UTF-8">
<title>LED Lighting Flyer</title>
<link href="https://fonts.googleapis.com/css2?family=Open+Sans:ital,wght@0,300;0,400;0,600;0,700;0,800;1,400;1,700&display=swap" rel="stylesheet">
<style>
  :root {
    --green: #1fa34a;
    --green-dark: #178a3c;
    --yellow: #e0b22c;
    --grey: #6d6e71;
    --white: #ffffff;
  }
  * { margin: 0; padding: 0; box-sizing: border-box; }
  html, body { width: 868px; height: 1200px; overflow: hidden; background: var(--white); }
  body { font-family: "Open Sans", Arial, sans-serif; color: var(--grey); }
  .flyer { position: relative; width: 868px; height: 1200px; overflow: hidden; background: var(--white); }
  .shape { position: absolute; display: block; }
  .shape--corner-top-left { left: 0; top: 56px; }
  .shape--corner-top-right { left: 677px; top: 56px; }
  .shape--corner-bottom-right { left: 680px; top: 930px; }

  .headline { position: absolute; right: 45px; top: 192px; text-align: right; color: var(--green); }
  .headline__title { font-size: 32px; font-weight: 400; line-height: 1.1; }
  .headline__sub { font-size: 16px; font-style: italic; color: var(--grey); }

  .facts { position: absolute; left: 169px; top: 272px; width: 240px; }
  .facts__label { color: var(--green); font-weight: 700; font-size: 15px; margin-bottom: 6px; }
  .facts__text { font-size: 21px; font-weight: 300; line-height: 1.08; margin-bottom: 18px; letter-spacing: -0.4px; }

  .think-green { position: absolute; left: 450px; top: 270px; width: 200px; height: 112px; }
  .think-green__text {
    position: absolute; left: 14px; top: 22px; color: var(--white);
    font-size: 18px; font-weight: 300; line-height: 1.15;
  }
  .think-green__text b { font-weight: 700; }

  .bulb-art {
    position: absolute; left: 655px; top: 272px; width: 150px; height: 170px;
    background: radial-gradient(circle at 50% 40%, #ffd23a 0 28%, #f6a21d 42%, rgba(246,162,29,0.15) 64%, transparent 66%);
  }

  .arrow-icon { position: absolute; left: 169px; top: 474px; }
  .pattern { position: absolute; left: 169px; top: 540px; }

  .offer { position: absolute; left: 388px; top: 474px; width: 390px; }
  .offer__question { color: var(--green); font-weight: 700; font-size: 24px; line-height: 1.2; }
  .offer__answer { color: var(--green); font-weight: 400; font-size: 21px; line-height: 1.3; margin-bottom: 24px; }
  .offer__body { font-size: 16px; font-weight: 300; line-height: 1.3; }

  .banner { position: absolute; left: 169px; top: 760px; width: 392px; height: 113px; background: var(--yellow); }
  .banner__text {
    position: absolute; left: 30px; top: 46px; color: var(--white);
    font-size: 17px; font-weight: 300; letter-spacing: -0.3px;
  }
  .banner__text b { font-weight: 700; }

  .slogan {
    position: absolute; left: 636px; top: 758px; color: var(--green);
    font-size: 34px; line-height: 1.02; text-transform: uppercase; font-weight: 300;
  }
  .slogan b { font-weight: 700; }

  .brand { position: absolute; left: 169px; top: 990px; width: 480px; height: 190px; }
  .brand__mark { position: absolute; left: 0; top: 22px; width: 56px; height: 56px; background: var(--green); }
  .brand__name {
    position: absolute; left: 74px; top: 0; color: var(--green);
    font-weight: 800; font-size: 76px; line-height: 1; letter-spacing: -1px;
  }
  .brand__tagline {
    position: absolute; left: 2px; top: 150px; color: var(--green);
    font-weight: 700; font-size: 16px; letter-spacing: 1.5px; font-style: italic;
  }
</style>
</head>
<body>
<main class="flyer">
  <svg class="shape shape--corner-top-left" width="293" height="136" viewBox="0 0 293 136" aria-hidden="true">
    <polygon points="0,0 293,0 0,136" fill="var(--green)"/>
  </svg>
  <svg class="shape shape--corner-top-right" width="146" height="147" viewBox="0 0 146 147" aria-hidden="true">
    <polygon points="0,0 146,0 146,147" fill="var(--green)"/>
  </svg>

  <header class="headline">
    <h1 class="headline__title">Using leds</h1>
    <p class="headline__sub">you can help the planet</p>
  </header>

  <section class="facts">
    <h2 class="facts__label">Did you know?</h2>
    <p class="facts__text">With the help of LED's you will save up to 90% of the electricity bill, it helps the planet!</p>
    <p class="facts__text">They don't contain mercury, release carbon dioxide.</p>
  </section>

  <div class="think-green">
    <svg class="shape" width="200" height="112" viewBox="0 0 200 112" aria-hidden="true">
      <polygon points="0,0 200,0 0,112" fill="var(--green)"/>
    </svg>
    <p class="think-green__text">Think<br><b>Green.</b></p>
  </div>

  <div class="bulb-art" role="img" aria-label="Illustration of a glowing light bulb with a hand inside"></div>

  <svg class="arrow-icon" width="40" height="40" viewBox="0 0 42 42" aria-hidden="true">
    <circle cx="21" cy="21" r="18" fill="none" stroke="var(--green-dark)" stroke-width="3"/>
    <path d="M12 21 H29 M22 14 L29 21 L22 28" fill="none" stroke="var(--green-dark)" stroke-width="3" stroke-linecap="round" stroke-linejoin="round"/>
  </svg>

  <svg class="pattern" width="150" height="150" viewBox="0 0 150 150" aria-hidden="true">
    <polygon points="150,0 150,75 75,75" fill="var(--green)"/>
    <polygon points="75,75 75,150 0,150" fill="var(--green)"/>
    <polygon points="75,75 150,75 75,150" fill="var(--green)"/>
  </svg>

  <section class="offer">
    <h2 class="offer__question">Do you want to save money?</h2>
    <p class="offer__answer">The LED light bulbs are the solution!</p>
    <p class="offer__body">they resist at lower temperatures, aren't sensitive to humidity, there haven't been any registered case of catching fire, release a bad odor or smoke from them, unlike incandescent and halogen bulbs.</p>
  </section>

  <div class="banner">
    <p class="banner__text">Think<b>different.</b></p>
  </div>

  <p class="slogan">Just<br>make it<br><b>simple</b><br>&amp; <b>green</b></p>

  <svg class="shape shape--corner-bottom-right" width="143" height="135" viewBox="0 0 143 135" aria-hidden="true">
    <polygon points="143,0 143,135 0,135" fill="var(--green)"/>
  </svg>

  <div class="brand">
    <span class="brand__mark" aria-hidden="true"></span>
    <span class="brand__name">Brightfold</span>
    <p class="brand__tagline">LIGHTING UP YOUR FUTURE</p>
  </div>
</main>
</body>
</html>
```